A start-up named "brivora" - a clinical research organization needs a new PowerPoint design

We need a new PowerPoint Design (incl. business card and stationery design) for an early-stage start-up named "brivora" seeking to build an ecosystem/ strategic partner alliances or consortium of committed and active collaborators to guide important components of the clinical trial.

Our ultimate goal is to avoid false neutrals – therapies that have not been and may never be evaluated in clinical trials due to the costs and/ or complexity.

The final design should highlight our patient-centric approach, innovative study design supported with the novel AI platform to make a stronger impact on patient lives.

Please see the attached brief for more details.
Updates

Requesting the proposals on color-coding, business-card designs, clinical research visuals, and icons as well as stationery design.

Target Market(s)

Pharma/ Biotech Executives
Medical Institutions
Clinical Trial Participants (Patients)

Colors
e34398

Requirements
Must have
• Use the Color Version of purple/ magenta logo

```html
<!DOCTYPE html>
<html lang="en">
<head>
<meta charset="utf-8">
<title>brivora stationery and business card design</title>
<link rel="stylesheet" href="https://fonts.googleapis.com/css2?family=Ubuntu:wght@400;500;700&family=Open+Sans:wght@300&display=swap">
<style>
:root{
  --stage:#e6e6e6;
  --paper:#f4f4f4;
  --white:#ffffff;
  --brand:#c8146e;
  --brand-soft:#e34398;
  --pink-strong:#f8b2d9;
  --pink-light:#fde8f2;
  --ink:#2b2b2b;
  --rule:#9a9a9a;
  --title:#8c8c8c;
}
*{margin:0;padding:0;box-sizing:border-box}
html,body{width:1200px;height:633px;overflow:hidden;background:var(--stage);font-family:"Ubuntu",sans-serif;color:var(--ink)}
.canvas{position:relative;width:1200px;height:633px}
.item{position:absolute}
.logo{position:absolute;display:flex;align-items:center;gap:.22em;font-family:"Ubuntu",sans-serif;font-weight:700;color:var(--brand);line-height:1;letter-spacing:-.01em}
.logo-mark{display:inline-block;width:.42em;height:.42em;background:var(--brand);margin-top:-.5em}
.address{position:absolute;background:linear-gradient(135deg,var(--pink-strong),var(--pink-light));font-size:4.6px;line-height:1.3;padding:6px 5px 0 8px;color:var(--ink)}
.address b{font-weight:700;font-size:5.4px}

/* envelope */
.envelope{left:243px;top:133px;width:259px;height:129px;background:var(--paper)}
.envelope .address{left:174px;top:87px;width:61px;height:42px;font-size:4.6px;padding:11px 10px}
.envelope .address b{font-size:5.6px}

/* letterhead */
.letterhead{left:531px;top:133px;width:245px;height:346px;background:linear-gradient(135deg,var(--pink-light),var(--pink-strong))}
.letterhead-sheet{position:absolute;left:7px;top:7px;right:7px;bottom:7px;background:var(--paper);border:1px solid var(--brand-soft)}
.letterhead .address{left:31px;top:275px;width:43px;height:63px;font-size:2.6px;padding:15px 7px 0}
.letterhead .address b{font-size:3.4px}

/* folder */
.folder{left:808px;top:133px;width:253px;height:365px;background:linear-gradient(160deg,var(--pink-strong) 0%,#fcd3e8 50%,var(--pink-light) 100%)}
.rule{position:absolute;height:2px;background:var(--brand)}
.url{position:absolute;font-size:5px;color:var(--brand)}

/* business cards */
.card-front{left:115px;top:311px;width:101px;height:65px;background:linear-gradient(135deg,var(--pink-strong),var(--pink-light))}
.card-front-inner{position:absolute;left:5px;top:5px;right:5px;bottom:5px;background:var(--white);border:1px solid var(--brand-soft)}
.card-back{left:236px;top:309px;width:101px;height:66px;background:var(--white)}
.card-back-panel{position:absolute;left:57px;top:0;right:0;bottom:0;background:linear-gradient(135deg,var(--pink-strong),var(--pink-light));font-size:2.3px;line-height:1.3;padding:16px 3px 0 7px}
.card-back-panel b{font-size:3.6px}
.holder{position:absolute;left:7px;top:35px;font-size:5px;line-height:1.2}
.holder b{font-size:5.2px;font-weight:700}
.holder i{display:block;width:7px;height:1px;background:var(--brand);margin:2px 0}

/* notebook */
.notebook{left:366px;top:305px;width:132px;height:178px;background:linear-gradient(150deg,#f2b6d8,#f6d3e5 55%,#f5cde2)}
.spiral{left:366px;top:295px;width:132px;height:16px}

/* title band */
.title-band{position:absolute;left:0;top:561px;width:1200px;height:72px;background:var(--white)}
.title-band h1{position:absolute;left:0;right:0;top:15px;text-align:center;font-family:"Open Sans",sans-serif;font-weight:300;font-size:30px;letter-spacing:.36em;color:var(--title);padding-left:.36em}
.title-band .line{position:absolute;top:34px;height:1px;background:var(--rule)}
</style>
</head>
<body>
<main class="canvas">

  <section class="item envelope" aria-label="Envelope">
    <div class="logo" style="left:174px;top:24px;font-size:14px">brivora<span class="logo-mark"></span></div>
    <div class="address"><b>Brivora GmbH</b><br>Street name 1<br>9999 City name<br>Switzerland</div>
  </section>

  <section class="item letterhead" aria-label="Letterhead">
    <div class="letterhead-sheet"></div>
    <div class="logo" style="left:31px;top:33px;font-size:20px">brivora<span class="logo-mark"></span></div>
    <div class="address"><b>Brivora GmbH</b><br>Street name 1<br>9999 City name<br>Switzerland<br><br>O: +41 (0)12 345 60 00<br>P: +41 (0)12 345 67 89<br>M: +41 (0)98 765 43 21<br>F: +41 (0)12 345 60 01<br><br>name.surname@brivora.ch<br>www.brivora.ch</div>
  </section>

  <section class="item folder" aria-label="Presentation folder">
    <div class="rule" style="left:0;top:59px;width:185px"></div>
    <div class="logo" style="left:91px;top:80px;font-size:27px">brivora<span class="logo-mark"></span></div>
    <div class="url" style="left:137px;top:108px">www.brivora.ch</div>
    <div class="rule" style="left:91px;top:132px;width:162px"></div>
  </section>

  <section class="item card-front" aria-label="Business card front">
    <div class="card-front-inner"></div>
    <div class="logo" style="left:26px;top:27px;font-size:11px">brivora<span class="logo-mark"></span></div>
  </section>

  <section class="item card-back" aria-label="Business card back">
    <div class="logo" style="left:7px;top:18px;font-size:8px">brivora<span class="logo-mark"></span></div>
    <div class="holder"><b>Name Surname</b><i></i>PhD<br>Managing Partner</div>
    <div class="card-back-panel"><b>Brivora GmbH</b><br>Street name 1<br>9999 City name<br>Switzerland<br><br>O: +41 (0)12 345 60 00<br>P: +41 (0)12 345 67 89<br>M: +41 (0)98 765 43 21<br>F: +41 (0)12 345 60 01<br><br>name.surname@brivora.ch<br>www.brivora.ch</div>
  </section>

  <section class="item notebook" aria-label="Notebook cover">
    <div class="rule" style="left:0;top:121px;width:95px;height:1px"></div>
    <div class="logo" style="left:47px;top:134px;font-size:14px">brivora<span class="logo-mark"></span></div>
    <div class="url" style="left:70px;top:150px;font-size:3px">www.brivora.ch</div>
    <div class="rule" style="left:47px;top:158px;width:85px;height:1px"></div>
  </section>
  <svg class="item spiral" viewBox="0 0 132 16" aria-hidden="true">
    <g fill="none" stroke="var(--brand)" stroke-width="1.6" stroke-linecap="round">
      <path d="M8 14 V6 a2 2 0 0 1 4 0"/><path d="M21 14 V6 a2 2 0 0 1 4 0"/><path d="M34 14 V6 a2 2 0 0 1 4 0"/>
      <path d="M47 14 V6 a2 2 0 0 1 4 0"/><path d="M60 14 V6 a2 2 0 0 1 4 0"/><path d="M73 14 V6 a2 2 0 0 1 4 0"/>
      <path d="M86 14 V6 a2 2 0 0 1 4 0"/><path d="M99 14 V6 a2 2 0 0 1 4 0"/><path d="M112 14 V6 a2 2 0 0 1 4 0"/>
      <path d="M125 14 V6 a2 2 0 0 1 4 0"/>
    </g>
  </svg>

  <footer class="title-band">
    <span class="line" style="left:0;width:159px"></span>
    <h1>STATIONERY &amp; BUSINESS CARD DESIGN</h1>
    <span class="line" style="left:1038px;width:162px"></span>
  </footer>

</main>
</body>
</html>
```